BrivoPeak Business Card Design Project

We are looking for a modern, clean business card design for our new company. We are a consulting firm focused on the financial services market providing management and IT consulting to banks, insurance companies, etc. Please include our company logo and company contact information from the attached file in the design. Two versions of the logo are attached, either version is acceptable. Logos are available in other file formats if needed. We would like to include the contact information for both our UK and US offices as well as the following information for each individual card holder: Name, position/title, address, phone number and e-mail address.
Updates
Project Deadline Extended
Reason: A last minute trip over seas has prevented us from finalizing the decision. A decision will be made this week. We apologize for the inconvenience.
Industry/Entity Type
Business
Contact Information for Business Card
Company logo.
Company locations and phone numbers for both the US and UK offices.
Company URL.
Cardholder Name
Cardholder Position/title
Cardholder Address
Cardholder Phone Number
Cardholder e-mail Address
Look and feel
Each slider illustrates characteristics of the customer's brand and the style your logo design should communicate.

```html
<!DOCTYPE html>
<html lang="en">
<head>
<meta charset="utf-8">
<title>BrivoPeak Partners – Business Card</title>
<link rel="stylesheet" href="https://fonts.googleapis.com/css2?family=Open+Sans:wght@400;600;700&display=swap">
<style>
  :root {
    --navy: #17305c;
    --navy-deep: #102447;
    --grey: #6b6d70;
    --grey-light: #9a9c9f;
    --text: #3a3b3d;
    --white: #ffffff;
    --page: #e9eaec;
  }
  * { box-sizing: border-box; margin: 0; padding: 0; }
  html, body {
    width: 1200px; height: 900px; overflow: hidden;
    background: var(--page);
    font-family: "Open Sans", Arial, sans-serif;
  }
  .sheet {
    position: relative; width: 1200px; height: 900px;
  }
  .card {
    position: absolute; left: 285px;
    width: 630px; height: 360px;
    border-radius: 6px; overflow: hidden;
    box-shadow: 0 6px 18px rgba(0,0,0,.18);
  }
  .card-back { top: 50px; background: var(--navy); }
  .card-front { top: 470px; background: var(--white); }
  .card-art { position: absolute; inset: 0; }

  /* back */
  .back-name {
    position: absolute; right: 48px; top: 70px;
    text-align: right; color: var(--white);
  }
  .back-name .company {
    font-weight: 700; font-size: 34px; letter-spacing: .3px; line-height: 1.1;
  }
  .back-name .rule {
    display: block; height: 2px; width: 180px; margin: 8px 0 0 auto;
    background: var(--white); opacity: .8;
  }

  /* front */
  .brand {
    position: absolute; left: 260px; top: 78px; width: 320px;
    text-align: center; color: var(--navy);
    font-weight: 700; font-size: 32px; line-height: 1.1;
  }
  .brand .mark {
    display: block; width: 34px; height: 34px; margin: 0 auto 10px;
    background: var(--navy);
  }
  .brand .rule {
    display: block; height: 2px; width: 250px; margin: 8px auto 0;
    background: var(--grey);
  }
  .holder {
    position: absolute; left: 70px; top: 158px; color: var(--text);
  }
  .holder .name { font-weight: 700; font-size: 20px; color: var(--navy); line-height: 1.1; }
  .holder .title { font-size: 16px; color: var(--grey); margin-bottom: 12px; }
  .address { font-size: 14px; line-height: 1.3; color: var(--text); }
  .contact-list { list-style: none; margin-top: 12px; }
  .contact-list li {
    display: flex; align-items: center; gap: 10px;
    font-size: 16px; line-height: 1.55; color: var(--text);
  }
  .contact-list svg { width: 14px; height: 14px; fill: var(--navy); flex: none; }
  .office-us {
    position: absolute; left: 340px; top: 232px;
  }
</style>
</head>
<body>
<main class="sheet">

  <section class="card card-back" aria-label="Business card back">
    <svg class="card-art" viewBox="0 0 630 360" aria-hidden="true">
      <rect width="630" height="360" fill="var(--navy)"/>
      <line x1="430" y1="150" x2="610" y2="120" stroke="#ffffff" stroke-opacity=".25" stroke-width="2"/>
    </svg>
    <div class="back-name">
      <div class="company">BrivoPeak Partners</div>
      <span class="rule"></span>
    </div>
  </section>

  <section class="card card-front" aria-label="Business card front">
    <svg class="card-art" viewBox="0 0 630 360" aria-hidden="true">
      <rect width="630" height="360" fill="var(--navy)"/>
      <path d="M20,60 C60,10 200,0 330,0 L630,0 L630,30 C650,150 640,280 560,340 C520,360 460,360 420,360 L60,360 C10,330 0,280 0,220 L0,110 C0,90 8,72 20,60 Z" fill="var(--white)"/>
      <path d="M0,150 C0,80 40,20 180,8 C240,3 300,4 340,8" fill="none" stroke="var(--grey-light)" stroke-width="6"/>
      <path d="M0,180 C4,100 50,40 200,22" fill="none" stroke="var(--grey)" stroke-width="3"/>
      <path d="M610,40 C640,170 610,290 520,346" fill="none" stroke="var(--grey)" stroke-width="7"/>
      <path d="M625,110 C630,230 590,320 500,360" fill="none" stroke="var(--grey-light)" stroke-width="3"/>
      <path d="M0,290 L0,360 L80,360 C40,345 10,320 0,290 Z" fill="var(--navy)"/>
    </svg>

    <div class="brand">
      <span class="mark"></span>
      BrivoPeak Partners
      <span class="rule"></span>
    </div>

    <div class="holder">
      <div class="name">Add Name</div>
      <div class="title">Manager</div>
      <p class="address">14-16 Marlow Street London<br>E2 4QT Great Britain</p>
      <ul class="contact-list">
        <li><svg viewBox="0 0 24 24"><path d="M6.6 10.8a15.1 15.1 0 0 0 6.6 6.6l2.2-2.2a1 1 0 0 1 1-.25 11.4 11.4 0 0 0 3.6.57 1 1 0 0 1 1 1V20a1 1 0 0 1-1 1A17 17 0 0 1 3 4a1 1 0 0 1 1-1h3.5a1 1 0 0 1 1 1c0 1.25.2 2.45.57 3.57a1 1 0 0 1-.25 1z"/></svg>(555) 014-2280</li>
        <li><svg viewBox="0 0 24 24"><path d="M6.6 10.8a15.1 15.1 0 0 0 6.6 6.6l2.2-2.2a1 1 0 0 1 1-.25 11.4 11.4 0 0 0 3.6.57 1 1 0 0 1 1 1V20a1 1 0 0 1-1 1A17 17 0 0 1 3 4a1 1 0 0 1 1-1h3.5a1 1 0 0 1 1 1c0 1.25.2 2.45.57 3.57a1 1 0 0 1-.25 1z"/></svg>+44 7700 900418</li>
        <li><svg viewBox="0 0 24 24"><circle cx="12" cy="12" r="10" fill="none" stroke="var(--navy)" stroke-width="2"/><path d="M2 12h20M12 2c3 3 3 17 0 20M12 2c-3 3-3 17 0 20" fill="none" stroke="var(--navy)" stroke-width="1.6"/></svg>www.brivopeakpartners.com</li>
      </ul>
    </div>

    <p class="address office-us">218 N Harbor Ave, Suite 402-118<br>Lakeford UT 84120<br>United States</p>
  </section>

</main>
</body>
</html>
```